Mobile Game identical to "Letter Orbit"

We need a design for mobile game identical to "Letter Orbit" you can get from app store using this link https://quickstorelink.example/us/tzvnR.k
playstore link: https://apps.samplemarket.example/store/apps/details?id=se.fenwoodgames.letterorbit&hl=en

- App name will be : Tangle
- For iOS and Android
- Same Letter Orbit features exactly but in different design.
- Ads banner will be overall app screens
- Some kind of animation is needed in the game , designer has to provide.

Requirements
Must have
• - Same Letter Orbit Features and steps
• - Some Animation
• - Game will be in arabic i will help to provide needed text

```html
<!DOCTYPE html>
<html lang="en">
<head>
<meta charset="utf-8">
<title>Tangle – Level Select</title>
<link rel="stylesheet" href="https://fonts.googleapis.com/css2?family=Roboto+Slab:wght@800&family=Roboto+Condensed:wght@700&display=swap">
<style>
  :root {
    --wood-light: #f1ddbd;
    --wood-mid: #e6cba2;
    --wood-dark: #d9b98b;
    --board: #3a3836;
    --board-edge: #2b2a28;
    --frame-outer: #9a5424;
    --frame-inner: #d88a48;
    --text-light: #ffffff;
    --text-soft: #e8e4de;
    --title-ink: #e07a9c;
    --icon-snail: #c9a978;
    --icon-squid: #a6417a;
    --icon-fish: #5cc6c9;
    --icon-crab: #e0483c;
    --icon-chicken: #e88a2a;
    --icon-duck: #efb23a;
  }
  * { box-sizing: border-box; margin: 0; padding: 0; }
  html, body { width: 683px; height: 1200px; overflow: hidden; }
  body {
    background: linear-gradient(90deg, var(--wood-mid), var(--wood-light) 30%, var(--wood-mid) 55%, var(--wood-light) 80%, var(--wood-dark));
    font-family: "Roboto Slab", Georgia, serif;
  }
  .screen { width: 683px; height: 1200px; position: relative; }
  .top-bar {
    height: 130px;
    display: flex;
    align-items: center;
    justify-content: center;
    position: relative;
  }
  .back-button {
    position: absolute;
    left: 28px;
    top: 42px;
    width: 50px;
    height: 44px;
  }
  .app-title {
    font-size: 58px;
    color: var(--title-ink);
    letter-spacing: 2px;
    text-transform: lowercase;
  }
  .level-list {
    list-style: none;
    padding: 18px 20px 0;
    display: flex;
    flex-direction: column;
    gap: 30px;
  }
  .level-card {
    height: 146px;
    border: 8px solid var(--frame-outer);
    box-shadow: inset 0 0 0 4px var(--frame-inner), inset 0 0 0 10px var(--board-edge), 0 4px 6px rgba(0,0,0,.25);
    background: var(--board);
    border-radius: 4px;
    display: flex;
    align-items: center;
    padding: 0 40px 0 34px;
  }
  .level-icon {
    width: 96px;
    height: 86px;
    border-radius: 16px;
    flex: none;
  }
  .level-info { margin-left: 30px; flex: 1; }
  .level-name {
    color: var(--text-light);
    font-size: 36px;
    letter-spacing: 2px;
    line-height: 1.1;
  }
  .level-size {
    font-family: "Roboto Condensed", Arial, sans-serif;
    color: var(--text-soft);
    font-size: 24px;
    margin-top: 6px;
  }
  .level-state { width: 34px; height: 40px; flex: none; }
</style>
</head>
<body>
<main class="screen">
  <header class="top-bar">
    <svg class="back-button" viewBox="0 0 50 44" aria-label="Back">
      <path d="M22 6 L6 22 L22 38 M6 22 H46 M18 14 L10 22 L18 30" fill="none" stroke="#2e2a26" stroke-width="5" stroke-linecap="round" stroke-linejoin="round"/>
    </svg>
    <h1 class="app-title">Tangle</h1>
  </header>

  <ul class="level-list">
    <li class="level-card">
      <div class="level-icon" role="img" aria-label="Snail icon" style="background:var(--icon-snail)"></div>
      <div class="level-info"><div class="level-name">SNAIL</div><div class="level-size">SIZE 2X2</div></div>
      <svg class="level-state" viewBox="0 0 34 40" aria-label="Open"><path d="M10 6 L24 20 L10 34" fill="none" stroke="#fff" stroke-width="5" stroke-linecap="round" stroke-linejoin="round"/></svg>
    </li>
    <li class="level-card">
      <div class="level-icon" role="img" aria-label="Squid icon" style="background:var(--icon-squid)"></div>
      <div class="level-info"><div class="level-name">SQUID</div><div class="level-size">SIZE 2X2</div></div>
      <svg class="level-state" viewBox="0 0 34 40" aria-label="Open"><path d="M10 6 L24 20 L10 34" fill="none" stroke="#fff" stroke-width="5" stroke-linecap="round" stroke-linejoin="round"/></svg>
    </li>
    <li class="level-card">
      <div class="level-icon" role="img" aria-label="Fish icon" style="background:var(--icon-fish)"></div>
      <div class="level-info"><div class="level-name">FISH</div><div class="level-size">SIZE 2X2</div></div>
      <svg class="level-state" viewBox="0 0 34 40" aria-label="Open"><path d="M10 6 L24 20 L10 34" fill="none" stroke="#fff" stroke-width="5" stroke-linecap="round" stroke-linejoin="round"/></svg>
    </li>
    <li class="level-card">
      <div class="level-icon" role="img" aria-label="Crab icon" style="background:var(--icon-crab)"></div>
      <div class="level-info"><div class="level-name">CRAB</div><div class="level-size">SIZE 3X3</div></div>
      <svg class="level-state" viewBox="0 0 34 40" aria-label="Locked"><path d="M10 18 V12 a7 7 0 0 1 14 0 V18" fill="none" stroke="#fff" stroke-width="4"/><rect x="5" y="18" width="24" height="18" rx="3" fill="#fff"/></svg>
    </li>
    <li class="level-card">
      <div class="level-icon" role="img" aria-label="Chicken icon" style="background:var(--icon-chicken)"></div>
      <div class="level-info"><div class="level-name">CHICKEN</div><div class="level-size">SIZE 3X3</div></div>
      <svg class="level-state" viewBox="0 0 34 40" aria-label="Locked"><path d="M10 18 V12 a7 7 0 0 1 14 0 V18" fill="none" stroke="#fff" stroke-width="4"/><rect x="5" y="18" width="24" height="18" rx="3" fill="#fff"/></svg>
    </li>
    <li class="level-card">
      <div class="level-icon" role="img" aria-label="Duck icon" style="background:var(--icon-duck)"></div>
      <div class="level-info"><div class="level-name">DUCK</div><div class="level-size">SIZE 3X3</div></div>
      <svg class="level-state" viewBox="0 0 34 40" aria-label="Locked"><path d="M10 18 V12 a7 7 0 0 1 14 0 V18" fill="none" stroke="#fff" stroke-width="4"/><rect x="5" y="18" width="24" height="18" rx="3" fill="#fff"/></svg>
    </li>
  </ul>
</main>
</body>
</html>
```